Packaging for Hair Fibers Product

We are a start up company looking for a new packaging design for hair building fibers. These are aimed at predominantly men but also women as well. We already have a logo and i have the packaging design from our competitors. We are wanting to keep the look masculine as 90% of our users will be middle aged men. We would like the colours to be black and white but are open to other colours as well.
It will need to have our logo and the following somewhere on the front.
"Instant Fuller & Thicker Hair" & "Natural Hair Building Fibers" "28g" or "Net Weight 28g"
We only need the front of the packaging designed, please make the other sides of the packaging the same colour but blank.
Target Market(s)
Men 25+
Industry/Entity Type
Hair And Beauty
Requirements
Must have
- Logo which i have included. and the following somewhere on the front.
- "Instant Fuller & Thicker Hair" ; "Natural Hair Building Fibers" "28g" or "Net Weight 28g"
Nice to have
- Make it stand out from the competition or similar to the brantiq example.

```html
<!DOCTYPE html>
<html lang="en">
<head>
<meta charset="utf-8">
<title>Densora Pro – Hair Building Fibers Box</title>
<link href="https://fonts.googleapis.com/css2?family=Josefin+Sans:wght@300&family=Open+Sans:wght@400&family=Arimo:wght@400&display=swap" rel="stylesheet">
<style>
  :root {
    --page: #ffffff;
    --box-black: #231f20;
    --box-side: #3f3f41;
    --band-white: #ffffff;
    --ink-dark: #231f20;
    --ink-light: #ffffff;
  }
  html, body {
    margin: 0;
    padding: 0;
    width: 1200px;
    height: 1200px;
    overflow: hidden;
    background: var(--page);
  }
  .box-side {
    position: absolute;
    left: 0;
    top: 0;
    width: 1200px;
    height: 1200px;
  }
  .box-side polygon {
    fill: var(--box-side);
  }
  .front-panel {
    position: absolute;
    left: 360px;
    top: 118px;
    width: 528px;
    height: 975px;
    background: var(--box-black);
    color: var(--ink-light);
    text-align: center;
  }
  .brand-band {
    position: absolute;
    left: 0;
    top: 244px;
    width: 100%;
    height: 151px;
    background: var(--band-white);
  }
  .brand-name {
    position: absolute;
    left: 0;
    right: 0;
    top: 38px;
    margin: 0;
    padding-left: 4px;
    font-family: "Josefin Sans", sans-serif;
    font-weight: 300;
    font-size: 78px;
    line-height: 1;
    letter-spacing: 4px;
    color: var(--ink-dark);
  }
  .brand-sub {
    position: absolute;
    right: 45px;
    top: 108px;
    font-family: "Arimo", sans-serif;
    font-size: 21px;
    line-height: 1;
    letter-spacing: 7px;
    color: var(--ink-dark);
  }
  .product-type {
    position: absolute;
    left: 0;
    right: 0;
    top: 418px;
    margin: 0;
    font-family: "Arimo", sans-serif;
    font-size: 29px;
    line-height: 1;
    letter-spacing: 0.5px;
  }
  .headline {
    position: absolute;
    left: 88px;
    right: 0;
    top: 524px;
    margin: 0;
    text-align: left;
    font-family: "Open Sans", sans-serif;
    font-weight: 400;
    font-size: 50px;
    line-height: 70px;
    letter-spacing: 1.5px;
  }
  .audience-badge {
    position: absolute;
    left: 204px;
    top: 721px;
    width: 122px;
    height: 122px;
    border-radius: 50%;
    background: var(--band-white);
    color: var(--ink-dark);
    display: flex;
    flex-direction: column;
    justify-content: center;
    font-family: "Arimo", sans-serif;
    font-size: 30px;
    line-height: 34px;
    letter-spacing: 1px;
  }
  .net-weight {
    position: absolute;
    left: 0;
    right: 0;
    top: 891px;
    margin: 0;
    font-family: "Arimo", sans-serif;
    font-size: 36px;
    line-height: 1;
  }
</style>
</head>
<body>
  <svg class="box-side" viewBox="0 0 1200 1200" aria-hidden="true">
    <polygon points="360,118 312,156 312,982 360,1093"/>
  </svg>
  <main class="front-panel">
    <div class="brand-band">
      <h1 class="brand-name">DENSORA</h1>
      <span class="brand-sub">PRO</span>
    </div>
    <p class="product-type">Natural Hair Building Fibers</p>
    <h2 class="headline">Instant Fuller<br>&amp; Thicker Hair</h2>
    <div class="audience-badge"><span>FOR</span><span>MEN</span></div>
    <p class="net-weight">28g</p>
  </main>
</body>
</html>
```